Unique business card design

Boutique coastal hotel suites - in need of clever stand out business card I have uploaded the logo that I had created through quill forge I want something that is clever and stands out from everyone else - 418 Brantwell Avenue kestrel cove Norland 99571 phone or text 555 -581-6142 www.primemarrowbysuites.com

Target Market(s)

Men and woman

Industry/Entity Type

Boutique coastal hotel

Contact Information for Business Card

Marrowby Suites kestrel cove Norland marrowby_suites@mailnest.net

Requirements
Must have
• Classy - clever -bold 907-581-6142 call or text

```html
<!DOCTYPE html>
<html lang="en">
<head>
<meta charset="utf-8">
<title>Marrowby Suites Business Card</title>
<link rel="stylesheet" href="https://fonts.googleapis.com/css2?family=Oswald:wght@500&family=Roboto:wght@400&display=swap">
<style>
  :root {
    --backdrop: #3a3a3a;
    --paper: #efebe4;
    --navy: #2f4a6b;
    --ink-grey: #5a5a5a;
    --rule-grey: #9a9a9a;
    --rule-dark: #1a1a1a;
    --accent-red: #c8322f;
  }
  * { margin: 0; padding: 0; box-sizing: border-box; }
  html, body {
    width: 1200px; height: 900px; overflow: hidden;
    background: var(--backdrop);
  }
  .stage {
    width: 1200px; height: 900px;
    display: flex; align-items: center; justify-content: center; gap: 60px;
  }
  .card {
    width: 525px; height: 300px;
    background: var(--paper);
    position: relative;
    box-shadow: 0 6px 18px rgba(0,0,0,0.35);
  }
  /* Contact side */
  .identity {
    position: absolute; right: 290px; top: 112px;
    text-align: right;
  }
  .identity__name {
    font-family: "Oswald", sans-serif; font-weight: 500;
    font-size: 34px; letter-spacing: 0.5px; color: var(--navy);
    text-transform: uppercase; line-height: 1;
  }
  .identity__role {
    font-family: "Roboto", sans-serif; font-size: 13px;
    color: var(--ink-grey); margin-top: 6px;
  }
  .divider {
    position: absolute; left: 255px; top: 100px;
    width: 1px; height: 100px; background: var(--rule-grey);
  }
  .contact {
    position: absolute; left: 272px; top: 104px;
    list-style: none;
    font-family: "Roboto", sans-serif; font-size: 13.5px;
    color: var(--ink-grey); line-height: 19px;
  }
  .contact li { display: flex; align-items: center; gap: 6px; white-space: nowrap; }
  .contact svg { width: 11px; height: 11px; fill: var(--navy); flex: none; }
  /* Brand side */
  .brand {
    position: absolute; inset: 0;
    display: flex; flex-direction: column; align-items: center; justify-content: center;
  }
  .brand__lockup { display: flex; align-items: center; gap: 12px; }
  .brand__mark { width: 18px; height: 18px; background: var(--accent-red); }
  .brand__name {
    font-family: "Roboto", sans-serif; font-weight: 400;
    font-size: 40px; letter-spacing: 3px; color: var(--navy);
    text-transform: uppercase;
  }
  .brand__rule {
    width: 310px; height: 2px; background: var(--rule-dark); margin-top: 18px;
  }
</style>
</head>
<body>
<main class="stage">
  <section class="card card--contact">
    <div class="identity">
      <h1 class="identity__name">Daniel Harrow</h1>
      <p class="identity__role">Director</p>
    </div>
    <div class="divider"></div>
    <ul class="contact">
      <li>418 Brantwell Avenue</li>
      <li>kestrel cove Norland 99571</li>
      <li><svg viewBox="0 0 12 12"><path d="M2.5 1l2 2.2-1 1.3a7 7 0 0 0 4 4l1.3-1 2.2 2-1.5 1.5C5 10.5 1.5 7 1 2.5z"/></svg>555 -581-6142</li>
      <li><svg viewBox="0 0 12 12"><path d="M1 2.5h10v7H1zM1.8 3.2L6 6.5l4.2-3.3v.9L6 7.4 1.8 4.1z" fill-rule="evenodd"/></svg>primemarrowbysuites.com</li>
      <li><svg viewBox="0 0 12 12"><circle cx="6" cy="6" r="5"/></svg>primemarrowbysuites.com</li>
    </ul>
  </section>
  <section class="card card--brand">
    <div class="brand">
      <div class="brand__lockup">
        <span class="brand__mark"></span>
        <span class="brand__name">Marrowby Suites</span>
      </div>
      <div class="brand__rule"></div>
    </div>
  </section>
</main>
</body>
</html>
```